E-brochure to promote our franchise opportunity to potential finance professionals

We need my words putting into a brochure, setting out, adding photographs and images ready for publication as a .pdf
The brochure needs to be readable as a pdf, I have no plans to publish on paper so should be well structured for a screen or tablet - easy navigation and a positive and striking visual feel

Target Market(s)

Potential business owners in business finance arranging - existing business bankers leaving their post, mortgage brokers expanding their business or existing commercial finance brokers looking for a means to expand their reach and have the help and support of a franchisor organisation

Industry/Entity Type

Finance

Font styles to use
Serif
Script

Colors
0555a3
eaf2ce

Requirements
Must have
• The project must have a professional but still accessible feel, we are not aiming to be a "corporate" like a merchant bank, our clients are ordinary small business owners, like you, so we need to speak their language. Our business is about the people we help, the dreams that come true because we help them and the wealth we create for them.
Nice to have
• Great artwork, interesting photographs, a compelling front cover page, pages which are easily readable, not too text heavy but getting the point across
Should not have
• Should not be boring - over corporate or too frivolous

```html
<!DOCTYPE html>
<html lang="en">
<head>
<meta charset="utf-8">
<title>Franchise Opportunity Brochure</title>
<link href="https://fonts.googleapis.com/css2?family=Kalam:wght@400;700&family=Lato:wght@400;700&display=swap" rel="stylesheet">
<style>
  :root {
    --brand-blue: #0555a3;
    --deep-navy: #1d2f5a;
    --soft-grey: #a9b3ba;
    --line-grey: #cfd3d6;
    --panel-grey: #e2e4e6;
    --paper: #ffffff;
    --backdrop: #ececec;
    --body-ink: #2b2b2b;
  }
  * { box-sizing: border-box; margin: 0; padding: 0; }
  html, body { width: 1200px; height: 1200px; overflow: hidden; background: var(--backdrop); }
  .stage {
    position: relative; width: 1400px; height: 1400px;
    transform: scale(0.857143); transform-origin: 0 0;
  }
  .page {
    position: absolute; width: 445px; height: 625px; background: var(--paper);
    overflow: hidden; box-shadow: 0 6px 18px rgba(0,0,0,0.25);
    font-family: 'Lato', sans-serif;
  }
  .page--cover { left: 193px; top: 48px; }
  .page--summary { left: 827px; top: 48px; }
  .page--back { left: 503px; top: 727px; }
  .page svg.shapes { position: absolute; inset: 0; width: 445px; height: 625px; }

  .brand { position: absolute; text-align: center; }
  .brand__name {
    font-family: 'Lato', sans-serif; font-weight: 700; color: var(--deep-navy);
    font-size: 22px; letter-spacing: 0.5px; display: flex; align-items: center; gap: 8px; justify-content: center;
  }
  .brand__dot { width: 12px; height: 12px; border-radius: 50%; background: var(--brand-blue); }
  .brand__tagline { font-family: 'Lato', sans-serif; font-size: 9px; color: var(--soft-grey); margin-top: 2px; }
  .page--cover .brand { left: 120px; top: 50px; width: 210px; }

  .cover-title { position: absolute; left: 60px; top: 130px; width: 330px; text-align: center; font-family: 'Kalam', cursive; font-weight: 700; line-height: 1; }
  .cover-title__top { color: var(--brand-blue); font-size: 50px; display: block; }
  .cover-title__bottom { color: var(--soft-grey); font-size: 52px; display: block; margin-top: 4px; }

  .header-bars { position: absolute; top: 20px; left: 35px; display: flex; gap: 6px; }
  .header-bars span { display: block; width: 121px; height: 4px; background: var(--brand-blue); }
  .header-bars span.is-grey { background: var(--soft-grey); }
  .summary-label {
    position: absolute; left: 36px; top: 44px; font-size: 10px; color: var(--brand-blue);
    text-decoration: underline; text-underline-offset: 2px; letter-spacing: 0.2px;
  }
  .section { position: absolute; left: 33px; width: 377px; }
  .section__head { display: flex; align-items: center; gap: 7px; font-family: 'Kalam', cursive; font-weight: 700; font-size: 12px; color: var(--deep-navy); }
  .section__head svg { width: 14px; height: 14px; flex: none; }
  .section__body { margin-left: 22px; margin-top: 3px; font-size: 7.6px; line-height: 10.5px; color: var(--body-ink); text-align: justify; }
  .section__list { margin-left: 14px; margin-top: 4px; list-style: none; font-size: 7.6px; color: var(--body-ink); }
  .section__list li { position: relative; padding-left: 8px; margin-bottom: 5px; }
  .section__list li::before { content: ""; position: absolute; left: 0; top: 3px; width: 4px; height: 4px; border-radius: 50%; background: var(--brand-blue); }

  .page--back .brand { left: 110px; top: 210px; width: 225px; }
  .page--back .brand__name { font-size: 21px; }
  .contact { position: absolute; left: 0; top: 296px; width: 445px; text-align: center; font-size: 10.5px; color: #1a1a1a; list-style: none; }
  .contact li { display: flex; justify-content: center; align-items: flex-start; gap: 6px; line-height: 12px; margin-bottom: 5px; }
  .contact svg { width: 11px; height: 11px; flex: none; margin-top: 1px; }
</style>
</head>
<body>
<div class="stage">

  <section class="page page--cover">
    <svg class="shapes" viewBox="0 0 445 625">
      <defs>
        <linearGradient id="coverPhoto" x1="0" y1="0" x2="1" y2="1">
          <stop offset="0" stop-color="#cdb892"/>
          <stop offset="0.45" stop-color="#e7e3da"/>
          <stop offset="1" stop-color="#c9d3de"/>
        </linearGradient>
      </defs>
      <polygon points="0,235 150,352 0,400" fill="var(--panel-grey)"/>
      <line x1="0" y1="178" x2="148" y2="326" stroke="var(--brand-blue)" stroke-width="3"/>
      <polygon points="335,0 445,0 445,103" fill="var(--brand-blue)"/>
      <line x1="305" y1="0" x2="410" y2="106" stroke="var(--line-grey)" stroke-width="4"/>
      <polygon points="0,405 445,290 445,625 0,625" fill="url(#coverPhoto)" role="img" aria-label="Photo of stacked coins beside an alarm clock on banknotes"/>
      <polygon points="0,398 445,283 445,290 0,405" fill="var(--brand-blue)"/>
    </svg>
    <div class="brand">
      <div class="brand__name"><span class="brand__dot"></span>Birchway Finance</div>
      <div class="brand__tagline">Backing local firms and their growth</div>
    </div>
    <h1 class="cover-title">
      <span class="cover-title__top">Franchise</span>
      <span class="cover-title__bottom">Opportunity</span>
    </h1>
  </section>

  <section class="page page--summary">
    <svg class="shapes" viewBox="0 0 445 625">
      <defs>
        <linearGradient id="summaryPhoto" x1="0" y1="0" x2="1" y2="1">
          <stop offset="0" stop-color="#b9a58d"/>
          <stop offset="0.5" stop-color="#dfe6ee"/>
          <stop offset="1" stop-color="#9fb4cc"/>
        </linearGradient>
      </defs>
      <polygon points="0,484 445,392 445,625 0,625" fill="url(#summaryPhoto)" role="img" aria-label="Photo of a person working a calculator over printed financial charts"/>
      <polygon points="0,477 445,385 445,392 0,484" fill="var(--brand-blue)"/>
      <polygon points="340,625 445,625 445,526" fill="var(--brand-blue)"/>
      <line x1="318" y1="625" x2="428" y2="530" stroke="var(--line-grey)" stroke-width="4"/>
    </svg>
    <div class="header-bars"><span></span><span class="is-grey"></span><span></span></div>
    <div class="summary-label">EXECUTIVE SUMMARY</div>

    <div class="section" style="top:70px">
      <div class="section__head"><svg viewBox="0 0 16 16"><circle cx="8" cy="8" r="6.5" fill="none" stroke="var(--brand-blue)" stroke-width="1.6"/><path d="M4.8 8.2 7.2 10.5 13.5 3.5" fill="none" stroke="var(--brand-blue)" stroke-width="1.8"/></svg>Objective</div>
      <p class="section__body">Now in its 20th year Birchway Finance is one of the UK's leading commercial finance brokers. It is our aim to broaden our customer base and to grow into a national UK name by the opening of Birchway Finance branches throughout the country. Small business is the lifeblood of the UK economy yet the high street banks pay lip-service to providing full support. Contrast this with the hundreds of other lenders in the market and there is a healthy level of funding available for the small business yet many are unaware of the options available to them. More than 60% of small business owners begin and end their search for finance with their own bank, regardless of success.</p>
    </div>
    <div class="section" style="top:186px">
      <div class="section__head"><svg viewBox="0 0 16 16"><circle cx="8" cy="8" r="6.5" fill="none" stroke="var(--brand-blue)" stroke-width="1.6"/><path d="M4.8 8.2 7.2 10.5 13.5 3.5" fill="none" stroke="var(--brand-blue)" stroke-width="1.8"/></svg>Goals</div>
      <p class="section__body">It is our goal to grow the broker introduced business finance sector to similar levels to those of the insurance or residential mortgage markets and to make the name Birchway Finance as well known as the high street banks.</p>
    </div>
    <div class="section" style="top:247px">
      <div class="section__head"><svg viewBox="0 0 16 16"><circle cx="8" cy="8" r="6.5" fill="none" stroke="var(--brand-blue)" stroke-width="1.6"/><path d="M4.8 8.2 7.2 10.5 13.5 3.5" fill="none" stroke="var(--brand-blue)" stroke-width="1.8"/></svg>Solution</div>
      <p class="section__body">In order to facilitate this growth Birchway Finance will be available as a franchise to ambitious finance professionals, existing commercial brokers looking to strengthen their product offering and market presence and to commercial bankers looking to grow their careers outside the corporate structure.</p>
    </div>
    <div class="section" style="top:322px">
      <div class="section__head"><svg viewBox="0 0 16 16"><circle cx="8" cy="8" r="6.5" fill="none" stroke="var(--brand-blue)" stroke-width="1.6"/><path d="M4.8 8.2 7.2 10.5 13.5 3.5" fill="none" stroke="var(--brand-blue)" stroke-width="1.8"/></svg>Project Outline</div>
      <p class="section__body">Launching a market leading franchise network of professional commercial finance brokers with nationwide coverage.</p>
      <ul class="section__list">
        <li>Regional coverage.</li>
        <li>Local representation.</li>
        <li>Highest levels of customer service in the industry.</li>
      </ul>
    </div>
  </section>

  <section class="page page--back">
    <svg class="shapes" viewBox="0 0 445 625">
      <defs>
        <linearGradient id="backPhoto" x1="0" y1="0" x2="1" y2="1">
          <stop offset="0" stop-color="#f2f2f2"/>
          <stop offset="0.5" stop-color="#e6e6e6"/>
          <stop offset="1" stop-color="#f4f4f4"/>
        </linearGradient>
      </defs>
      <rect width="445" height="625" fill="url(#backPhoto)" role="img" aria-label="Faded photo of a hand signing documents at a desk"/>
      <polygon points="0,0 152,0 0,138" fill="var(--brand-blue)"/>
      <line x1="155" y1="0" x2="30" y2="124" stroke="var(--soft-grey)" stroke-width="4"/>
      <polygon points="445,503 445,625 322,625" fill="var(--brand-blue)"/>
      <line x1="306" y1="625" x2="405" y2="527" stroke="var(--soft-grey)" stroke-width="4"/>
    </svg>
    <div class="brand">
      <div class="brand__name"><span class="brand__dot"></span>Birchway Finance</div>
      <div class="brand__tagline">Backing local firms and their growth</div>
    </div>
    <ul class="contact">
      <li><svg viewBox="0 0 16 16"><path d="M3 1.5 6 1l1.5 3.5-2 1.3a8 8 0 0 0 4.7 4.7l1.3-2L15 10l-.5 3a2 2 0 0 1-2 1.5A12 12 0 0 1 1.5 3.5 2 2 0 0 1 3 1.5z" fill="var(--brand-blue)"/></svg>01632 960 418</li>
      <li><svg viewBox="0 0 16 16"><circle cx="8" cy="8" r="7.5" fill="var(--brand-blue)"/><rect x="4" y="5" width="8" height="6" fill="#fff"/><path d="M4 5 8 8.5 12 5" fill="none" stroke="var(--brand-blue)" stroke-width="1"/></svg>hello@birchwayfinance.co</li>
      <li><svg viewBox="0 0 16 16"><circle cx="8" cy="8" r="7" fill="var(--brand-blue)"/><path d="M1 8h14M8 1c-3 3-3 11 0 14M8 1c3 3 3 11 0 14" fill="none" stroke="#fff" stroke-width="0.9"/></svg>www.birchwayfinance.co</li>
      <li><svg viewBox="0 0 16 16"><path d="M8 1a4.5 4.5 0 0 0-4.5 4.5C3.5 9 8 14 8 14s4.5-5 4.5-8.5A4.5 4.5 0 0 0 8 1z" fill="var(--brand-blue)"/><circle cx="8" cy="5.5" r="1.6" fill="#fff"/><rect x="2" y="14" width="12" height="1.5" fill="var(--brand-blue)"/></svg><span>12 Millfield Business Park,<br>Harrogate. HG1 2QT</span></li>
    </ul>
  </section>

</div>
</body>
</html>
```